Brochure Design Project The Quiet Willow

Very tight deadline** Please accept only if you can start working as soon as possible**The Quiet Willow is a personal concierge business. I have already used Sketchwharf for a logo and postcards. Thanks! I can send content after you layout the text. Thanks again!<br/>** I also want the front to somehow include the following "Personal Concierge Services - Affordable Rates."

Target Market(s)

working class to affluent

Font styles to use
Serif

Requirements
Must have
• PLEASE SEE BROCHURE PRINTING TEMPLATE. I will send content. The layout must be eye catching and visually appealing. I am looking to send to printer by 3 p.m. EST tomorrow. Please begin designing asap! Thank you!

```html
<!DOCTYPE html>
<html lang="en">
<head>
<meta charset="utf-8">
<title>The Quiet Willow – Brochure Inside Spread</title>
<link rel="stylesheet" href="https://fonts.googleapis.com/css2?family=Cormorant+Garamond:ital,wght@0,700;1,700&family=Didact+Gothic&display=swap">
<style>
  :root {
    --paper: #ffffff;
    --grass-light: #7fae3e;
    --grass-mid: #5c8f2c;
    --grass-dark: #3f6e1d;
    --panel: rgba(62, 112, 40, 0.72);
    --ink-light: #ffffff;
    --photo-blue: #2a6f9e;
    --photo-warm: #5a6e3a;
    --gift-light: #e9d8b4;
    --gift-dark: #d2b88a;
    --mark: #222222;
  }
  * { margin: 0; padding: 0; box-sizing: border-box; }
  html, body { width: 1200px; height: 941px; overflow: hidden; background: var(--paper); }
  .sheet { position: relative; width: 1200px; height: 941px; background: var(--paper); }

  .print-marks { position: absolute; inset: 0; }

  .spread {
    position: absolute; left: 30px; top: 30px; width: 1140px; height: 880px; overflow: hidden;
    background:
      radial-gradient(ellipse at 30% 20%, rgba(160, 200, 90, 0.35), transparent 60%),
      radial-gradient(ellipse at 70% 80%, rgba(40, 80, 20, 0.3), transparent 60%),
      linear-gradient(160deg, var(--grass-light), var(--grass-mid) 50%, var(--grass-dark));
  }

  .photo-portrait {
    position: absolute; left: 740px; top: 0; width: 400px; height: 400px;
    background: linear-gradient(200deg, var(--photo-blue), var(--photo-warm));
    opacity: 0.9;
  }
  .photo-gift {
    position: absolute; left: 820px; top: 490px; width: 320px; height: 390px;
    background: linear-gradient(160deg, var(--gift-light), var(--gift-dark));
  }

  .panel {
    position: absolute; background: var(--panel); border-radius: 22px;
    color: var(--ink-light); text-align: center;
    font-family: "Didact Gothic", "Century Gothic", sans-serif;
    font-size: 17.5px; line-height: 17.3px;
  }
  .panel--lifestyle { left: 40px; top: 70px; width: 300px; height: 736px; padding-top: 35px; }
  .panel--care { left: 422px; top: 340px; width: 298px; height: 466px; padding-top: 60px; }

  .panel-title {
    font-family: "Cormorant Garamond", Georgia, serif; font-weight: 700;
    font-size: 35px; line-height: 31px; margin-bottom: 24px; white-space: nowrap;
  }
  .panel--care .panel-title { margin-bottom: 22px; }
  .service { margin-bottom: 25px; }
  .service-title {
    font-family: "Cormorant Garamond", Georgia, serif; font-weight: 700;
    font-size: 30px; line-height: 24px; white-space: nowrap;
  }
  .service p { white-space: nowrap; }

  .brand {
    position: absolute; left: 398px; top: 88px; width: 340px; text-align: center; color: var(--ink-light);
  }
  .brand-name {
    font-family: "Cormorant Garamond", Georgia, serif; font-weight: 700;
    font-size: 48px; line-height: 56px; white-space: nowrap;
  }
  .brand-service {
    font-family: "Didact Gothic", sans-serif; font-size: 23px; line-height: 26px;
    margin-top: 15px; font-weight: 700; white-space: nowrap;
  }
  .brand-tagline {
    display: flex; align-items: center; justify-content: center; gap: 8px; margin-top: 0;
    font-family: "Cormorant Garamond", Georgia, serif; font-style: italic; font-weight: 700;
    font-size: 27px; line-height: 30px; white-space: nowrap;
  }
  .brand-tagline::before, .brand-tagline::after {
    content: ""; width: 48px; height: 2px; background: var(--ink-light);
  }
</style>
</head>
<body>
<div class="sheet">
  <svg class="print-marks" width="1200" height="941" aria-hidden="true">
    <g class="gray-bar">
      <rect x="38" y="0" width="21" height="20" fill="#000"/>
      <rect x="59" y="0" width="21" height="20" fill="#1e1e1e"/>
      <rect x="80" y="0" width="21" height="20" fill="#3a3a3a"/>
      <rect x="101" y="0" width="21" height="20" fill="#555"/>
      <rect x="122" y="0" width="21" height="20" fill="#707070"/>
      <rect x="143" y="0" width="21" height="20" fill="#8c8c8c"/>
      <rect x="164" y="0" width="21" height="20" fill="#a8a8a8"/>
      <rect x="185" y="0" width="21" height="20" fill="#c4c4c4"/>
      <rect x="206" y="0" width="21" height="20" fill="#dcdcdc"/>
      <rect x="227" y="0" width="21" height="20" fill="#eeeeee"/>
      <rect x="248" y="0" width="13" height="20" fill="#fff" stroke="#333" stroke-width="1"/>
    </g>
    <g class="color-bar">
      <rect x="938" y="0" width="20" height="20" fill="#ffec00"/>
      <rect x="958" y="0" width="20" height="20" fill="#e6007e"/>
      <rect x="978" y="0" width="20" height="20" fill="#00a0e3"/>
      <rect x="998" y="0" width="20" height="20" fill="#2b2f86"/>
      <rect x="1018" y="0" width="20" height="20" fill="#00963f"/>
      <rect x="1038" y="0" width="20" height="20" fill="#e30613"/>
      <rect x="1058" y="0" width="20" height="20" fill="#222"/>
      <rect x="1078" y="0" width="20" height="20" fill="#fff59b"/>
      <rect x="1098" y="0" width="20" height="20" fill="#f49ac1"/>
      <rect x="1118" y="0" width="20" height="20" fill="#6dc7ee"/>
      <rect x="1138" y="0" width="24" height="20" fill="#999"/>
    </g>
    <g class="crop-lines" stroke="var(--mark)" stroke-width="0.8">
      <line x1="0" y1="30" x2="20" y2="30"/><line x1="30" y1="920" x2="30" y2="941"/>
      <line x1="1180" y1="30" x2="1200" y2="30"/><line x1="1170" y1="920" x2="1170" y2="941"/>
      <line x1="0" y1="910" x2="20" y2="910"/><line x1="1180" y1="910" x2="1200" y2="910"/>
      <line x1="1170" y1="0" x2="1170" y2="20"/>
    </g>
    <g class="registration" fill="none" stroke="var(--mark)" stroke-width="1">
      <circle cx="600" cy="10" r="6"/><line x1="590" y1="10" x2="610" y2="10"/><line x1="600" y1="0" x2="600" y2="20"/>
      <circle cx="600" cy="930" r="6"/><line x1="590" y1="930" x2="610" y2="930"/><line x1="600" y1="920" x2="600" y2="940"/>
      <circle cx="10" cy="470" r="6"/><line x1="0" y1="470" x2="20" y2="470"/><line x1="10" y1="460" x2="10" y2="480"/>
      <circle cx="1189" cy="470" r="6"/><line x1="1179" y1="470" x2="1199" y2="470"/><line x1="1189" y1="460" x2="1189" y2="480"/>
    </g>
  </svg>

  <main class="spread">
    <div class="photo-portrait" role="img" aria-label="Photo: a relaxed woman in a blue top lying on the grass with eyes closed"></div>
    <div class="photo-gift" role="img" aria-label="Photo: a cream gift certificate envelope tied with a pale pink ribbon"></div>

    <header class="brand">
      <div class="brand-name">The Quiet Willow</div>
      <div class="brand-service">Personal Concierge Services</div>
      <div class="brand-tagline">Get Your Time Back.</div>
    </header>

    <section class="panel panel--lifestyle">
      <h2 class="panel-title">Personal Assistance<br>&amp; Lifestyle<br>Management</h2>
      <div class="service">
        <h3 class="service-title">Errand Services</h3>
        <p>Dry cleaning drop-off/pick-up<br>Prescription drop-off/pick-up<br>Post office runs<br>Grocery shopping</p>
      </div>
      <div class="service">
        <h3 class="service-title">Personal Services</h3>
        <p>Gift shopping/returns<br>Appointment scheduling<br>Home organization/de-<br>cluttering<br>Non-medical elder care (meal<br>prep &amp; errands)<br>Vacation planning/travel<br>research<br>Meal preparation<br>Arrangement of cleaning and<br>other home services<br>Internet searches &amp; price<br>comparison<br>Holiday preparation<br>Accommodation/<br>entertainment arrangement<br>for out-of-town guests</p>
      </div>
      <div class="service">
        <h3 class="service-title">Event-Planning</h3>
        <p>Dinner parties<br>Cocktail parties<br>Bridal and baby showers<br>Birthday &amp; graduation parties</p>
      </div>
    </section>

    <section class="panel panel--care">
      <h2 class="panel-title">Taking Care<br>Of You</h2>
      <div class="service">
        <h3 class="service-title">Pet Care</h3>
        <p>Vet visits<br>Grooming arrangements<br>Doggie day-care shuttle</p>
      </div>
      <div class="service">
        <h3 class="service-title">Relocation Services</h3>
        <p>Coordination with moving company<br>Unpacking and organization<br>In-home services arrangement<br>(cable, security, pest control, etc.)</p>
      </div>
      <div class="service">
        <h3 class="service-title">Waiting Services</h3>
        <p>Appliance &amp; computer repair<br>Home Repair<br>Deliveries</p>
      </div>
    </section>
  </main>
</div>
</body>
</html>
```